Inspirational music needs a cd cover design

This CD is an individual project (no company). It is meant to reach
as many people as possible with great, inspiring music. It will be
available by mail and at gigs.

The cover will be a 4-panel eco-wallet (front cover, back cover, left
and right inside panels). I have a template from the CD manufacturing
company.

Target Market(s)

I am aiming for a very broad market. That said, the median age will
likely be 40 years old, and the CD will particularly appeal to people
concerned about climate change and activism, especially in the U.S.

Industry/Entity Type

Colors

Designer to choose colors to be used in the design.

Requirements
Must have
• I have an image that I would like on the front cover, and on the CD
• itself. It is a photo of a painting. I also have a photo of me for the back cover. For the background on the inner 2 panels I don't have an image but would like an image of a sky with storm clouds as long as the text is clearly readable.
• Typefaces: For the informational text I'd like something easy to read, like Verdana. For the album title and my name on the front cover, two typeface examples I like are the cover of Lorne Becket Ensemble "Beyond the Harbor and Drifting" and Tobias Wrenly and Longbow "Hum Tide."

```html
<!DOCTYPE html>
<html lang="en">
<head>
<meta charset="utf-8">
<title>Inside Panel Credits</title>
<link rel="stylesheet" href="https://fonts.googleapis.com/css2?family=Noto+Sans:wght@400;700&display=swap">
<style>
  :root {
    --sky-deep: #16181f;
    --sky-mid: #2c313d;
    --sky-light: #4a505c;
    --text: #f2f3f5;
    --frame-green: #8fd6a0;
    --trim-pink: #e0709c;
    --trim-blue: #7aa6d8;
  }
  html, body {
    margin: 0;
    padding: 0;
    overflow: hidden;
    background: #ffffff;
  }
  .panel {
    position: relative;
    width: 1200px;
    height: 1032px;
    overflow: hidden;
    font-family: "Noto Sans", Verdana, sans-serif;
    color: var(--text);
  }
  .storm-sky {
    position: absolute;
    inset: 6px 0 0 0;
    background:
      radial-gradient(ellipse 60% 40% at 30% 30%, rgba(110,116,128,0.45), transparent 70%),
      radial-gradient(ellipse 50% 35% at 75% 60%, rgba(95,100,112,0.4), transparent 70%),
      radial-gradient(ellipse 70% 30% at 50% 95%, rgba(80,70,80,0.45), transparent 70%),
      linear-gradient(180deg, var(--sky-mid) 0%, var(--sky-deep) 45%, var(--sky-mid) 75%, var(--sky-light) 100%);
  }
  .trim {
    position: absolute;
    top: 6px;
    bottom: 0;
    width: 2px;
    background: var(--trim-pink);
  }
  .trim--left { left: 25px; }
  .trim--right { left: 1172px; }
  .edge {
    position: absolute;
    top: 6px;
    bottom: 0;
    width: 1px;
    background: var(--trim-blue);
  }
  .edge--left { left: 0; }
  .edge--right { right: 0; }
  .safe-frame {
    position: absolute;
    left: 52px;
    top: 24px;
    width: 1095px;
    height: 982px;
    border: 2px solid var(--frame-green);
    box-sizing: border-box;
  }
  .credits {
    position: absolute;
    left: 57px;
    top: 43px;
    width: 1090px;
    font-size: 22.4px;
    line-height: 29.6px;
    letter-spacing: 1px;
    white-space: nowrap;
  }
  .credits p { margin: 0; }
  .credits .intro { margin-bottom: 28px; }
  .credits .track { margin-bottom: 2px; }
  .credits .track-list { margin-bottom: 26px; }
  .credits .musician-key { margin-bottom: 26px; }
  .credits .studio-credits { margin-bottom: 29px; }
  .credits .thanks { margin-bottom: 39px; }
  .track-title { font-weight: 700; }
</style>
</head>
<body>
<div class="panel">
  <div class="storm-sky" role="img" aria-label="Photo of a dark sky filled with storm clouds"></div>
  <div class="edge edge--left"></div>
  <div class="edge edge--right"></div>
  <div class="trim trim--left"></div>
  <div class="trim trim--right"></div>
  <div class="safe-frame"></div>

  <div class="credits">
    <div class="intro">
      <p>All vocals, keyboards, acoustic guitar, and arranging RT except where noted</p>
      <p>All drums and percussion Kieran Dalton</p>
    </div>

    <div class="track-list">
      <p class="track"><span class="track-title">Song for the Rivermen:</span> backing vocals FB, IH/ organ FB/ saxophones and horn arr.<br>Nora Whitcomb/ trumpets Peter Valdane, Miles Corrigan/ bass PN/ arranging FB</p>
      <p class="track"><span class="track-title">Other Shores:</span> backing vocals NP, VL/ bass PN/ violin Dana Voss/ vocal arr. NP</p>
      <p class="track"><span class="track-title">Nell’s Midnight Junk Store:</span> bass LQ</p>
      <p class="track"><span class="track-title">Luminous:</span> backing vocals CM, NP/ bass LQ/ cello Owen Hartley</p>
      <p class="track"><span class="track-title">The Solar Tycoon:</span> backing vocals NP, RT/ bass PN/ elec. guitar HM/ “not an activist”<br>Ray Lombardelli/ vocal arr. NP, RT</p>
      <p class="track"><span class="track-title">Four Doors Out:</span> backing vocals IH/ elec. guitar FB/ bass PN/ “expanding” The Grabbler/ “the<br>world will end” Lena Hartwell/ other voices by real capitalists/ arranging FB</p>
      <p class="track"><span class="track-title">Homo Habilis:</span> bass PN/ elec. guitar WT</p>
      <p class="track"><span class="track-title">Frontlandia:</span> backing vocals NP, VL, RT/ vocal and synth arranging NP</p>
      <p class="track"><span class="track-title">Miriam’s Hands:</span> backing vocals NP, IH, RT/ bass PN/ elec. guitar WT/ glockenspiel NP/ vocal<br>arr. NP</p>
      <p class="track"><span class="track-title">Rise Now:</span> vocals CM, RT, NP/ elec. guitar HM/ bass PN/ vocal arr. NP</p>
      <p class="track"><span class="track-title">Will You March With Me:</span> backing vocals NP, VL/ bass PN/ saxes Glen Ravelle/ vocal arr. NP</p>
    </div>

    <p class="musician-key">HM: Hugo Marsh FB: Felix Brandt LQ: Leo Quinn PN: Paul Navarre IH: Iris Holden NP:<br>Nathan Price VL: Vera Lund CM: Carla Moss WT: Wes Tolland</p>

    <p class="studio-credits">All tracks recorded and mixed at Samsound Studio by Sam Whitley assisted by NP except #1 and<br>#6 at Fox Hollow Studio by Jared Mills. Assisted by FB. Mastered by Roland Gerstner<br>at Amber Mastering. Cover art: Adrian Pell, Photo: Ross Dunham, Layout: ______</p>

    <p class="thanks">Big, big thanks to Sam and Nathan for their extraordinary giving of themselves, to Mari-<br>anne for seeing the possible, and always to Tamar. And special gratitude to Brent Harlow<br>and Dan Lerner for their support.</p>

    <p class="easter-egg">There is a lost amphibian on this album; please let me know if you find him.</p>
  </div>
</div>
</body>
</html>
```